The (Private) News Sharing Report

This is a professional and academic report of 35 pages for journalists and teachers. The topic of the report is News Sharing: journalism, social networks and technology. Attached there is an example of the kind of design we are looking for: visual, fresh and modern.

Target Market(s)

Journalists, Journalism Students, Communication Researchers,

Industry/Entity Type

Media

Font styles to use
Sans Serif

Colors
3276b5
33a6d7
886aae
b868aa

Requirements
Must have
• Copyleft images, visual style
Nice to have
• There is an example attached.

```html
<!DOCTYPE html>
<html lang="en">
<head>
<meta charset="utf-8">
<title>The (Private) News Sharing Report — Spread 2–3</title>
<link href="https://fonts.googleapis.com/css2?family=Montserrat:wght@300;400;500;600;700;800&display=swap" rel="stylesheet">
<style>
  :root{
    --backdrop:#e9eaee;
    --page-dark:#353843;
    --page-light:#ffffff;
    --ink-dark:#2a2c33;
    --ink-light:#e4e6ec;
    --muted-light:#b9bcc6;
    --blue:#3276b5;
    --sky:#33a6d7;
    --violet:#886aae;
    --orchid:#b868aa;
    --watermark:#c9d2e8;
    --rule:#6b6f7c;
  }
  *{margin:0;padding:0;box-sizing:border-box}
  html,body{width:1200px;height:900px;overflow:hidden;background:var(--backdrop)}
  body{font-family:"Montserrat",sans-serif;position:relative}

  .spread{position:absolute;left:40px;top:70px;width:1120px;height:760px;display:flex;box-shadow:0 10px 30px rgba(0,0,0,.18)}
  .page{position:relative;width:560px;height:760px;overflow:hidden}

  /* Left page */
  .page--left{background:var(--page-dark);color:var(--ink-light)}
  .index{position:absolute;left:74px;top:262px;width:162px}
  .index__title{font-weight:300;font-size:38px;letter-spacing:.5px;color:#f2f3f6;margin-bottom:22px}
  .index__list{list-style:none}
  .index__item{display:flex;justify-content:space-between;font-size:11px;font-weight:600;padding:4px 0 4px;border-bottom:1px solid var(--rule);color:#f2f3f6}

  .thanks{position:absolute;left:385px;top:92px;width:150px}
  .thanks__title{font-weight:300;font-size:30px;line-height:1;color:#f2f3f6;letter-spacing:.5px}
  .thanks__sub{font-weight:700;font-size:20px;line-height:1;color:var(--orchid);margin-bottom:42px}
  .thanks__lead{font-size:7.6px;line-height:10.4px;font-weight:700;color:#f2f3f6;margin-bottom:12px}
  .thanks__body{font-size:7.6px;line-height:10.4px;color:var(--muted-light)}

  .network-left{position:absolute;left:460px;top:560px;width:100px;height:200px;
    background:radial-gradient(circle at 100% 60%,rgba(200,205,220,.22),rgba(53,56,67,0) 70%)}

  .folio{position:absolute;font-size:7.5px;letter-spacing:.3px;transform:rotate(-90deg);transform-origin:left top;white-space:nowrap}
  .folio--left{left:20px;bottom:8px;color:var(--muted-light)}
  .folio--right{left:534px;top:752px;color:var(--blue);font-weight:600}
  .folio b{font-weight:400;margin-right:6px;padding-right:6px;border-right:1px solid currentColor}

  /* Right page */
  .page--right{background:var(--page-light);color:var(--ink-dark)}
  .section-word{position:absolute;left:24px;top:760px;transform:rotate(-90deg);transform-origin:left top;
    font-weight:800;font-size:118px;line-height:.82;color:var(--watermark);letter-spacing:-1px;white-space:nowrap}
  .network-right{position:absolute;right:0;top:0;width:230px;height:270px;
    background:radial-gradient(ellipse at 85% 25%,rgba(51,166,215,.28),rgba(50,118,181,.08) 55%,rgba(255,255,255,0) 75%)}
  .intro{position:absolute;left:132px;top:266px;width:382px;columns:2;column-gap:14px;
    font-size:8.2px;line-height:10.3px;font-weight:500;color:var(--ink-dark)}
  .intro p{text-indent:10px}
  .intro p:first-child{text-indent:0}
  .drop{float:left;font-size:46px;line-height:36px;font-weight:300;color:var(--blue);margin:1px 3px 0 0}
</style>
</head>
<body>
<main class="spread">
  <section class="page page--left">
    <nav class="index">
      <h2 class="index__title">INDEX</h2>
      <ul class="index__list">
        <li class="index__item"><span>Introduction</span><span>4</span></li>
        <li class="index__item"><span>Research questions</span><span>5</span></li>
        <li class="index__item"><span>1. The Media Landscape</span><span>6</span></li>
        <li class="index__item"><span>2. The Interviews</span><span>11</span></li>
        <li class="index__item"><span>3. The Best Practices</span><span>29</span></li>
        <li class="index__item"><span>4. Conclusions</span><span>31</span></li>
        <li class="index__item"><span>5. References</span><span>33</span></li>
      </ul>
    </nav>

    <aside class="thanks">
      <h2 class="thanks__title">SPECIAL</h2>
      <p class="thanks__sub">thanks</p>
      <p class="thanks__lead">This is a report by Andrés Molina Ferrer (PhD), a journalist working at the Levante Catholic University (LCU, Spain), where he is the Head of the Communication Sciences Department. This project has been supported by a research grant from LCU to do a research stay as a Visiting Scholar at Capitol University (CU), USA, and the help of professor Martin Kessler at CU.</p>
      <p class="thanks__body">Special thanks goes to those who collaborated in the interviews: the journalists at the Global Center for Reporters (GCR), The Harbor Ledger, Meridian Media Network, Onda Visión, The Civic Accountability Desk, The Iberia Brief, Verifica and Contrasta. In addition, I also want to thank the whole faculty at the School of Communication at Capitol University, who always offered their collaboration.<br>Special thanks also goes to colleagues and scholars who selflessly dedicated their time to talk and hold meetings. They shed light on many topics reflected in the report. They are Elena Ruiz, Omar Haddad, Lucia Brenner, Paula Whitmore, Nora Castell, Tomás Ibarra, Victor Lang, and Grace Holden.<br>The interviews are expressions of personal opinions as journalists and they do not necessarily express the official point of view of the media where they work. Inquiries for further information about this research can be sent to amolina@mailbox.example or amolina@lcu.example</p>
    </aside>

    <div class="network-left" role="img" aria-label="Faint network of connected dots decoration"></div>
    <p class="folio folio--left"><b>2</b>The (Private) News Sharing Report</p>
  </section>

  <section class="page page--right">
    <div class="section-word" aria-hidden="true">Introduction</div>
    <div class="network-right" role="img" aria-label="Blue network of connected nodes and lines decoration"></div>

    <article class="intro">
      <p><span class="drop">T</span>he job of journalists is not just longer on the internet because it ends later, it is also longer because it starts before. On the web, on the one hand, a journalist can have a community even before having a journalistic product. On the other hand, social recommendations, incidental consumption of news and online private messages are giving a broader reach to journalism, as we know it now.</p>
      <p>Because publishing is not the end of the journalistic routine, the whole process now is longer. You cannot fully understand what “news” means for people if you do not understand how and why they are sharing the news on online private platforms. Private messaging networks are adding new challenges to journalists and the media. When we are talking about online private environments, issues such as sources, fact-checking, misinformation, privacy or (fake) news are being redefined, as well as the notions of trust, community, public service and media literacy.</p>
      <p>In 2018 a leading presidential candidate was accused of running a whole fake news campaign through ChatLine with hundreds of millions of messages against his opponent. This scandal is just an example of the growing relevance of fact-checking and the need to form media literacy skills among users of private messaging networks.</p>
      <p>Many news sites added a ChatLine sharing option in their news during the last few years (Harlow, 2014) and it seems like private channels, such as this one, could become a “major traffic driver for news sites” (Vance, A., Moreau, L., &amp; Tilde, K., 2015: 10). We cannot entirely know what people are doing with news in private messaging networks, but what we can see is what the media and journalists are doing with these platforms. This report is a draft of these actions.</p>
      <p>In news sharing research, a new broad theoretical foundation is needed, with quantitative studies, digital ethnographies or uses and gratifications approaches, and even combining these theories and deriving new ones. We utilize the results of this preliminary research to provide insights so that journalism can be improved, and academic research of journalism can move forward in news sharing research.</p>
      <p>The main goal of this executive report is to help journalists and researchers get a deeper understanding of the news sharing processes in private messaging apps, channels, and networks. Share it, but not in a private way. Make it as public as you can.</p>
    </article>

    <p class="folio folio--right"><b>3</b>Introduction</p>
  </section>
</main>
</body>
</html>
```